Card Design for my dog training business Rustpaw Obedience

Need a business card design for my dog training business with my new logo. Want the card to come off professional yet fun. Want it to be very eye catchy as well. I normally have these at vet clinics, pet stores, and groomers. so need it to look better than my competitors.
Target Market(s)
dog owners
Industry/Entity Type
Dog Training
Contact Information for Business Card
needs logo, my name and info
Font styles to use
Serif
Colors
0255a3
ffffff
ec1f27
000000
333333
fbfbfb
Requirements
Must have
- Rustpaw Obedience
- Hollis Brandt
- 415 903 2267
- info@rustpawobedience.example
- www.rustpawobedience.example

```html
<!DOCTYPE html>
<html lang="en">
<head>
<meta charset="utf-8">
<title>Rustpaw Obedience – Business Card</title>
<link rel="stylesheet" href="https://fonts.googleapis.com/css2?family=EB+Garamond:ital,wght@0,400;0,600;0,700;1,400&display=swap">
<style>
  :root {
    --brand-red: #ec1f27;
    --brand-blue: #0255a3;
    --white: #ffffff;
    --black: #000000;
    --ink: #333333;
    --paper: #fbfbfb;
    --paw-tint: #eef2f8;
    --stage: #5a5a5c;
  }
  * { box-sizing: border-box; margin: 0; padding: 0; }
  html, body {
    width: 1200px; height: 1200px; overflow: hidden;
    background: var(--stage);
    font-family: "EB Garamond", Georgia, serif;
  }
  .card {
    position: absolute;
    left: 181px;
    width: 838px;
    height: 478px;
    overflow: hidden;
  }
  .card--front { top: 101px; background: var(--brand-red); }
  .card--back { top: 631px; background: var(--white); }

  /* Front */
  .front-emblem {
    position: absolute; left: 257px; top: 69px; width: 296px; height: 202px;
    background: radial-gradient(ellipse at center, rgba(255,255,255,0.28), rgba(255,255,255,0.08));
    border-radius: 6px;
  }
  .wordmark {
    position: absolute; left: 0; width: 100%;
    display: flex; justify-content: center;
  }
  .wordmark__inner {
    border-top: 2px solid currentColor;
    border-bottom: 2px solid currentColor;
    padding: 10px 14px 8px;
    font-weight: 600;
    font-size: 34px;
    letter-spacing: 1px;
    line-height: 1;
    white-space: nowrap;
  }
  .card--front .wordmark { top: 285px; color: var(--white); }
  .tagline {
    position: absolute; left: 0; width: 100%;
    text-align: center; font-style: italic; font-size: 16px;
    white-space: nowrap;
  }
  .card--front .tagline { top: 390px; color: var(--white); }

  /* Back */
  .back-brand-panel {
    position: absolute; left: 0; top: 0; width: 414px; height: 100%;
    background: var(--paw-tint);
  }
  .back-emblem {
    position: absolute; left: 58px; top: 70px; width: 286px; height: 204px;
    background: linear-gradient(180deg, #f7d4d6 0%, #d9d9dc 60%, #bfc0c4 100%);
    border-radius: 6px;
  }
  .back-brand-panel .wordmark { top: 282px; color: var(--brand-blue); }
  .back-brand-panel .wordmark__inner { border-color: var(--black); font-size: 30px; }
  .back-brand-panel .tagline { top: 390px; color: var(--ink); font-size: 15px; }

  .holder-name {
    position: absolute; left: 414px; width: 424px; top: 50px;
    text-align: center; font-weight: 700; font-size: 38px; color: var(--black);
  }
  .contact-list {
    position: absolute; left: 470px; top: 345px; list-style: none;
  }
  .contact-list li {
    display: flex; align-items: center; height: 35px;
    font-weight: 700; font-size: 23px; color: var(--black);
    white-space: nowrap;
  }
  .contact-list svg { width: 14px; height: 14px; margin-right: 14px; flex: none; }
</style>
</head>
<body>

<section class="card card--front">
  <div class="front-emblem" role="img" aria-label="White line illustration of two dog heads inside a state outline"></div>
  <div class="wordmark"><span class="wordmark__inner">Rustpaw Obedience</span></div>
  <p class="tagline">“Patient lessons for every dog and every owner.”</p>
</section>

<section class="card card--back">
  <div class="back-brand-panel">
    <div class="back-emblem" role="img" aria-label="Black ink illustration of two dog heads inside a red state outline"></div>
    <div class="wordmark"><span class="wordmark__inner">Rustpaw Obedience</span></div>
    <p class="tagline">“Patient lessons for every dog and every owner.”</p>
  </div>

  <h1 class="holder-name">Hollis Brandt</h1>

  <ul class="contact-list">
    <li>
      <svg viewBox="0 0 16 16" aria-hidden="true"><path d="M4 1 L6.5 4 L5 6 C6 8.5 7.5 10 10 11 L12 9.5 L15 12 L13 15 C7 15 1 9 1 3 Z" fill="#ec1f27"/></svg>
      415 903 2267
    </li>
    <li>
      <svg viewBox="0 0 16 16" aria-hidden="true"><rect x="1" y="3" width="14" height="10" fill="#ec1f27"/><path d="M1 3 L8 9 L15 3" fill="none" stroke="#fff" stroke-width="1.4"/></svg>
      info@rustpawobedience.example
    </li>
    <li>
      <svg viewBox="0 0 16 16" aria-hidden="true"><g fill="none" stroke="#ec1f27" stroke-width="1.4"><circle cx="8" cy="8" r="6.5"/><ellipse cx="8" cy="8" rx="3" ry="6.5"/><path d="M1.5 8 H14.5 M2.5 5 H13.5 M2.5 11 H13.5"/></g></svg>
      www.rustpawobedience.example
    </li>
  </ul>
</section>

</body>
</html>
```